Kestrelway Advisory logo/business card design -- a digital consulting company

I've just restarted a consulting company I had years ago--Kestrelway Advisory. Now I need a new business card and updated logo. The original logo was simple enough: a chart-like progression atop a grid (see the attached file). I do strategy work, and the chart is meant to show incremental growth and profit. I'd like the reincarnation of my logo to be 3D, with both the grid and arrow rotated on their axis.

I'll want to use the logo on my website as well. I'm open to color schemes, fonts, etc.

Target Market(s)

Business-to-Business. Target market is corporate.

Industry/Entity Type

Business

Contact Information for Business Card

Logo on one-side; name and other contact info on the back

Font styles to use
Serif
Sans Serif

Requirements
Nice to have
• Kestrelway Advisory refers to the concept of "bootstrapping" or making incremental changes to grow with minimal risk and financial exposure, and self-sufficiency (think of the phrase "to pull oneself by one's bootstraps.")

```html
<!DOCTYPE html>
<html lang="en">
<head>
<meta charset="utf-8">
<title>Kestrelway Advisory — Business Card</title>
<link rel="stylesheet" href="https://fonts.googleapis.com/css2?family=Roboto:wght@300;400;700&display=swap">
<style>
  :root {
    --page: #e9ebee;
    --card-white: #ffffff;
    --brand-blue: #1a76c2;
    --ink-dark: #2b3340;
    --ink-body: #4a4f57;
    --band-slate: #4f6381;
    --band-steel: #566f97;
    --band-denim: #4977b3;
  }
  * { box-sizing: border-box; margin: 0; padding: 0; }
  html, body { width: 1200px; height: 873px; overflow: hidden; }
  body {
    background: var(--page);
    font-family: "Roboto", Arial, sans-serif;
    display: flex;
    align-items: center;
    justify-content: center;
    gap: 60px;
  }
  .card {
    width: 525px;
    height: 300px;
    position: relative;
    overflow: hidden;
    box-shadow: 0 6px 18px rgba(30, 40, 60, 0.18);
  }
  /* Contact side */
  .card--contact { background: var(--card-white); padding: 40px 44px; }
  .brand { display: flex; align-items: center; gap: 16px; }
  .brand__dot {
    width: 62px; height: 62px; border-radius: 50%;
    background: var(--brand-blue); flex: none;
  }
  .brand__name {
    color: var(--brand-blue); font-weight: 700;
    font-size: 19px; line-height: 1.15;
  }
  .contact { margin-top: 26px; color: var(--ink-body); font-weight: 300; font-size: 19px; line-height: 1.3; }
  .contact__name { color: var(--ink-dark); font-weight: 700; }
  .contact__web { margin-top: 14px; }
  /* Brand side */
  .card--brand { background: var(--brand-blue); }
  .card--brand svg { position: absolute; inset: 0; }
  .brand-mark {
    position: absolute; left: 190px; right: 30px; top: 0; bottom: 0;
    display: flex; align-items: center; justify-content: center;
    color: var(--card-white); font-weight: 700; font-size: 30px;
    line-height: 1.15; text-align: center;
  }
</style>
</head>
<body>
  <section class="card card--contact" aria-label="Business card, contact side">
    <div class="brand">
      <span class="brand__dot"></span>
      <p class="brand__name">Kestrelway<br>Advisory</p>
    </div>
    <div class="contact">
      <p class="contact__name">Name lastname</p>
      <p>email@email.com</p>
      <p>+1 2345 67890</p>
      <p class="contact__web">www.website.com</p>
    </div>
  </section>

  <section class="card card--brand" aria-label="Business card, brand side">
    <svg width="525" height="300" viewBox="0 0 525 300" aria-hidden="true">
      <polygon class="band" points="0,0 70,0 90,300 0,300" fill="var(--band-slate)"/>
      <polygon class="band" points="70,0 130,0 155,300 90,300" fill="var(--band-steel)"/>
      <polygon class="band" points="130,0 185,0 215,300 155,300" fill="var(--band-denim)"/>
    </svg>
    <p class="brand-mark">Kestrelway<br>Advisory</p>
  </section>
</body>
</html>
```